High-end residential home builder needs a business card design

We need a new business card design for a small residential construction company based in Boise, Idaho. We specialize in building custom high-end homes and remodels, with a focus on great design and craftsmanship.

We would like to use our current logo, but open to new color suggestions.
Just looking for a clean, sharp, modern design that looks high-end.

Target Market(s)

Upscale clientele

Industry/Entity Type

Contractor

Contact Information for Business Card

Company: Stonefield Custom Builders
Name: Marcus Tilley
Phone number: 208 367 4120
Email: MarcusTilleySCB@mailbox-example.com
Website: Stonefieldcustombuilders-example.com

Font styles to use
Serif
Sans Serif

Requirements
Must have
• Company Logo
Company name
My name
My phone number
My email
Company website
Nice to have
• I have attached a few photos of cards that I really like.

```html
<!DOCTYPE html>
<html lang="en">
<head>
<meta charset="utf-8">
<title>Stonefield Custom Builders – Business Card</title>
<link href="https://fonts.googleapis.com/css2?family=Arimo:wght@400;500&family=Montserrat:wght@500;600&display=swap" rel="stylesheet">
<style>
  :root {
    --backdrop: #1c1c1c;
    --card: #323232;
    --card-deep: #262626;
    --accent: #e08a1e;
    --ink-light: #f2f2f2;
    --ink-soft: #d9d9d9;
  }
  * { box-sizing: border-box; margin: 0; padding: 0; }
  html, body {
    width: 1200px; height: 901px; overflow: hidden;
    background: var(--backdrop);
  }
  .stage {
    width: 1200px; height: 901px;
    display: flex; align-items: center; justify-content: center; gap: 40px;
  }
  .card {
    width: 540px; height: 309px;
    background: var(--card);
    position: relative;
    box-shadow: 0 10px 30px rgba(0,0,0,.5);
  }

  /* Front */
  .card-front { display: flex; align-items: center; justify-content: center; gap: 18px; }
  .front-mark {
    width: 34px; height: 34px;
    border: 3px solid var(--card-deep);
  }
  .front-name {
    font-family: "Montserrat", sans-serif; font-weight: 600;
    font-size: 22px; letter-spacing: 5px; text-transform: uppercase;
    color: var(--card-deep); line-height: 1.35;
  }

  /* Back */
  .brand {
    position: absolute; left: 42px; top: 128px;
    display: flex; align-items: center; gap: 12px;
  }
  .brand-mark { width: 22px; height: 22px; border: 2px solid var(--ink-light); }
  .brand-name {
    font-family: "Montserrat", sans-serif; font-weight: 500;
    font-size: 12px; letter-spacing: 3.2px; text-transform: uppercase;
    color: var(--ink-light); line-height: 1.55;
  }
  .divider {
    position: absolute; left: 292px; top: 86px;
    width: 1px; height: 138px; background: var(--accent);
  }
  .contact-block {
    position: absolute; left: 312px; top: 86px;
    font-family: "Arimo", sans-serif;
  }
  .person-name { font-size: 23px; font-weight: 500; color: var(--accent); letter-spacing: -.2px; }
  .person-title { font-size: 12px; color: var(--ink-light); margin-top: 3px; }
  .contact-list { list-style: none; margin-top: 20px; }
  .contact-list li {
    display: flex; align-items: center; gap: 7px;
    font-size: 11px; color: var(--ink-soft); margin-bottom: 6px;
  }
  .contact-icon { width: 10px; height: 10px; flex: none; }
</style>
</head>
<body>
<main class="stage">
  <section class="card card-front" aria-label="Card front">
    <div class="front-mark"></div>
    <div class="front-name">Stonefield<br>Custom Builders</div>
  </section>

  <section class="card card-back" aria-label="Card back">
    <div class="brand">
      <div class="brand-mark"></div>
      <div class="brand-name">Stonefield<br>Custom Builders</div>
    </div>
    <div class="divider"></div>
    <div class="contact-block">
      <h1 class="person-name">Marcus Tilley</h1>
      <p class="person-title">Founder &amp; CEO</p>
      <ul class="contact-list">
        <li>
          <svg class="contact-icon" viewBox="0 0 10 10" aria-hidden="true"><path d="M2 0.5 L3.6 2.8 L2.7 3.8 Q3.7 6 6.2 7.3 L7.2 6.4 L9.5 8 L8.3 9.5 Q3 8.5 0.5 1.7 Z" fill="var(--accent)"/></svg>
          208 367 4120
        </li>
        <li>
          <svg class="contact-icon" viewBox="0 0 10 10" aria-hidden="true"><rect x="0.5" y="2" width="9" height="6.5" fill="var(--accent)"/><path d="M0.5 2 L5 5.8 L9.5 2" stroke="var(--card)" stroke-width="0.9" fill="none"/></svg>
          MarcusTilleySCB@mailbox-example.com
        </li>
        <li>
          <svg class="contact-icon" viewBox="0 0 10 10" aria-hidden="true"><circle cx="5" cy="5" r="4.5" fill="var(--accent)"/><path d="M0.5 5 H9.5 M5 0.5 Q2.5 5 5 9.5 M5 0.5 Q7.5 5 5 9.5" stroke="var(--card)" stroke-width="0.7" fill="none"/></svg>
          Stonefieldcustombuilders-example.com
        </li>
      </ul>
    </div>
  </section>
</main>
</body>
</html>
```